Derek Folsom Resume

Need to update resume with latest position and ensure it stays to 2 pages, may need advice on what to get rid of and simply clean it up, already have a format that i like but am open to change but don't want to spend a fortune

```html
<!DOCTYPE html>
<html lang="en">
<head>
<meta charset="utf-8">
<title>Derek Folsom – Resume</title>
<link href="https://fonts.googleapis.com/css2?family=PT+Sans:wght@400;700&display=swap" rel="stylesheet">
<style>
:root{
  --brand:#0069b4;
  --ink:#111;
  --dot-off:#e4e4e4;
  --paper:#fff;
}
*{margin:0;padding:0;box-sizing:border-box}
html,body{width:848px;height:1200px;overflow:hidden;background:var(--paper)}
body{font-family:"PT Sans",sans-serif;color:var(--ink);position:relative}
.abs{position:absolute}
.portrait{left:110px;top:61px;width:158px;height:158px}
.name{left:0;width:424px;top:234px;text-align:center;font-size:36px;font-weight:400;white-space:nowrap;padding-left:7px}
.role{left:0;width:404px;top:289px;text-align:center;font-size:28px;font-weight:700;line-height:35px}
.section-head{display:flex;align-items:center;gap:8px}
.section-head .icon{width:52px;height:52px;flex:none}
.section-head h2{font-size:28px;font-weight:700;color:var(--brand);letter-spacing:.2px;line-height:1}
.section-head .rule{height:3px;background:var(--brand);flex:1;margin-left:2px}
.head-profile{left:41px;top:389px;width:283px}
.head-contact{left:41px;top:664px;width:283px}
.head-skills{left:41px;top:874px;width:281px}
.head-experience{left:391px;top:62px;width:433px}
.profile-text{left:42px;top:448px;width:290px;font-size:10px;line-height:12.7px}
.profile-text p{margin-bottom:12.7px}
.contact-label{left:42px;color:var(--brand);font-weight:700;font-size:13px}
.contact-value{left:130px;font-size:13.5px;line-height:17px}
.skill{left:62px;width:244px;text-align:center}
.skill h3{font-size:16.5px;font-weight:400;margin-bottom:6px}
.dots{display:flex;gap:6.7px;justify-content:center}
.dots i{width:12px;height:12px;border-radius:50%;background:var(--dot-off)}
.dots i.on{background:var(--brand)}
.job{left:400px;top:141px;width:425px}
.job-line{display:flex;align-items:center;font-size:16px}
.job-line .bullet{width:13px;height:13px;border-radius:50%;background:var(--ink);margin-right:15px}
.job-line .company{font-weight:700;width:114px}
.job-title{font-size:16.5px;margin:3px 0 4px 27px}
.job-body{margin-left:29px;font-size:9.6px;line-height:12.7px}
.job-body .indent{padding-left:60px}
</style>
</head>
<body>

<svg class="abs portrait" viewBox="0 0 158 158" role="img" aria-label="Portrait photo of Derek Folsom">
  <circle cx="79" cy="79" r="78.5" fill="none" stroke="var(--brand)" stroke-width="1"/>
  <circle cx="79" cy="79" r="70" fill="var(--brand)"/>
</svg>

<h1 class="abs name">Derek W. Folsom</h1>
<div class="abs role">Award-Winning<br>Sales Manager</div>

<!-- Profile -->
<div class="abs section-head head-profile">
  <svg class="icon" viewBox="0 0 52 52"><circle cx="26" cy="26" r="25" fill="none" stroke="var(--brand)"/><circle cx="26" cy="26" r="22" fill="var(--brand)"/><circle cx="26" cy="20" r="6.5" fill="#fff"/><path d="M14 35c0-7 5-10 12-10s12 3 12 10z" fill="#fff"/></svg>
  <h2>PROFILE</h2><span class="rule"></span>
</div>
<div class="abs profile-text">
  <p>Driving exceptional levels of sales results in competitive industries and changing environments.</p>
  <p>Aggressive, loyal, energetic sales leader with a history of turning around underperforming teams,<br>departments, and territories. Proven consultative sales approach with a focus on product knowledge, trust,<br>and superior service. Strong interpersonal, communication, presentation, and analytical skills.</p>
  <p>&nbsp;&nbsp;&nbsp;- Developed effective sales incentives and initiatives that became company-wide best practices.<br>&nbsp;&nbsp;&nbsp;- Drove revenue growth at direct, indirect, and retail sales levels; won multiple prestigious awards.<br>&nbsp;&nbsp;&nbsp;&nbsp;-Recruited, developed, trained, and motivated high-energy sales/customer support teams.</p>
</div>

<!-- Contact -->
<div class="abs section-head head-contact">
  <svg class="icon" viewBox="0 0 52 52"><circle cx="26" cy="26" r="25" fill="none" stroke="var(--brand)"/><circle cx="26" cy="26" r="22" fill="var(--brand)"/><path d="M17 14l5-1 3 7-3 3c1 4 4 7 8 8l3-3 7 3-1 5c-1 2-3 2-5 2-11-2-18-9-19-19 0-2 0-4 2-5z" fill="#fff"/></svg>
  <h2>CONTACT</h2><span class="rule"></span>
</div>
<div class="abs contact-label" style="top:737px">ADDRESS</div>
<div class="abs contact-value" style="top:736px">1187 Larkspur Lane<br>Richmond, VA 23229</div>
<div class="abs contact-label" style="top:792px">E-MAIL</div>
<div class="abs contact-value" style="top:787px">dfolsom@inboxmail.net</div>
<div class="abs contact-label" style="top:830px">PHONE</div>
<div class="abs contact-value" style="top:824px;left:128px">757.555.0142</div>

<!-- Skills -->
<div class="abs section-head head-skills">
  <svg class="icon" viewBox="0 0 52 52"><circle cx="26" cy="26" r="25" fill="none" stroke="var(--brand)"/><circle cx="26" cy="26" r="22" fill="var(--brand)"/><path d="M26 11a9 9 0 0 0-5 16.5V31h10v-3.5A9 9 0 0 0 26 11z" fill="#fff"/><rect x="21" y="33" width="10" height="3" rx="1" fill="#fff"/><rect x="23" y="37.5" width="6" height="2.5" rx="1" fill="#fff"/></svg>
  <h2>SKILLS</h2><span class="rule"></span>
</div>
<div class="abs skill" style="top:941px"><h3>CREATIVE</h3><div class="dots"><i class="on"></i><i class="on"></i><i class="on"></i><i class="on"></i><i class="on"></i><i class="on"></i><i class="on"></i><i class="on"></i><i class="on"></i><i></i><i></i><i></i></div></div>
<div class="abs skill" style="top:993px"><h3>TEAMWORK</h3><div class="dots"><i class="on"></i><i class="on"></i><i class="on"></i><i class="on"></i><i class="on"></i><i class="on"></i><i class="on"></i><i class="on"></i><i class="on"></i><i class="on"></i><i class="on"></i><i></i></div></div>
<div class="abs skill" style="top:1045px"><h3>INNOVATE</h3><div class="dots"><i class="on"></i><i class="on"></i><i class="on"></i><i class="on"></i><i class="on"></i><i class="on"></i><i></i><i></i><i></i><i></i><i></i><i></i></div></div>
<div class="abs skill" style="top:1098px"><h3>COMMUNICATION</h3><div class="dots"><i class="on"></i><i class="on"></i><i class="on"></i><i class="on"></i><i class="on"></i><i class="on"></i><i class="on"></i><i class="on"></i><i class="on"></i><i class="on"></i><i class="on"></i><i></i></div></div>

<!-- Experience -->
<div class="abs section-head head-experience">
  <svg class="icon" viewBox="0 0 52 52"><circle cx="26" cy="26" r="25" fill="none" stroke="var(--brand)"/><circle cx="26" cy="26" r="22" fill="var(--brand)"/><path d="M21 20v-3a5 5 0 0 1 10 0v3" fill="none" stroke="#fff" stroke-width="2"/><rect x="14" y="20" width="24" height="17" rx="1.5" fill="#fff"/></svg>
  <h2>EXPERIENCE</h2><span class="rule"></span>
</div>
<div class="abs job">
  <div class="job-line"><span class="bullet"></span><span class="company">Vantrel</span><span>// 2014-Present</span></div>
  <div class="job-title">Developmental Executive</div>
  <div class="job-body">
    Sell wireless portfolio to the Department of Defense, Department of Homeland Security, Department of Justice, Harlow Meade Group, and Aerovane.<br>
    &nbsp;Increased overall revenue in assigned agencies 101.8% YOY.<br>
    <span class="indent">•</span>&nbsp;&nbsp;&nbsp;&nbsp;&nbsp;&nbsp;&nbsp;&nbsp;&nbsp;&nbsp;&nbsp;&nbsp;&nbsp;Wireless Solutions: Facilitate critical communications for U.S. federal government through wireless solutions for networks, infrastructures, and security and surveillance.<br>
    <span class="indent">•</span>&nbsp;&nbsp;&nbsp;&nbsp;&nbsp;&nbsp;&nbsp;&nbsp;&nbsp;&nbsp;&nbsp;&nbsp;&nbsp;Government Contracts: Navigate complex matrix of budgeting, bidding, and procurement for government contracts.<br>
    <span class="indent">•</span>&nbsp;&nbsp;&nbsp;&nbsp;&nbsp;&nbsp;&nbsp;&nbsp;&nbsp;&nbsp;&nbsp;&nbsp;&nbsp;Collaboration: Work closely with solution engineers, project managers, and C-level executives on identifying the best solutions for their organizations.
  </div>
</div>

</body>
</html>
```